Business card for Drone Aerial

I need a business card designed keeping in mind I want to do post cards also with a similar design.
Both sides of the card would be cool.
I have a skylark 5 max and would like a picture of it on the front of the card. Similar to one I attached.
I really like the look of a drone in the air and the background pic a little blurry. I attached a few images as IDEAS.
Some special things I want to be on the card additional to the normal business card info:
"Aerial Photography" or "Low Altitude Aerial Photography"?
"ZQB# 90817263"

I like modern and creative. My Favorite color is blue and I like blue on white.
I do not have a business name and am not going to have one. When they read "Aerial Photography" and see the drone and image they will know what the card is for.

FYI, The attached pictures are just images from framewillow and just samples/ideas.

Target Market(s)

Real estate, construction, events

Industry/Entity Type

Business

Contact Information for Business Card

Also Definitely want to contain, my name, my number and email address.

Requirements
Must have
• "ZQB# 90817263"
• "Aerial Photography"

```html
<!DOCTYPE html>
<html lang="en">
<head>
<meta charset="utf-8">
<title>Aerial Photography — Business Card</title>
<link rel="stylesheet" href="https://fonts.googleapis.com/css2?family=Montserrat:wght@400;600;700&family=Open+Sans:ital,wght@1,700&family=Great+Vibes&display=swap">
<style>
  :root {
    --stage: #6b7378;
    --sky-top: #4fa3f0;
    --sky-mid: #3f86ec;
    --sky-bottom: #2a40cc;
    --night-top: #0c1a4a;
    --night-mid: #1f3aa0;
    --night-bottom: #0a1230;
    --ink-light: #ffffff;
  }
  * { margin: 0; padding: 0; box-sizing: border-box; }
  html, body {
    width: 1200px; height: 900px; overflow: hidden;
    background: var(--stage);
  }
  .canvas {
    position: relative; width: 1200px; height: 900px;
    display: flex; flex-direction: column; align-items: center; justify-content: center; gap: 40px;
  }
  .card {
    position: relative; width: 660px; height: 378px; overflow: hidden;
    box-shadow: 0 10px 24px rgba(0,0,0,.3);
  }
  /* Card front */
  .card--front {
    background: linear-gradient(180deg, var(--sky-top) 0%, var(--sky-mid) 45%, var(--sky-bottom) 100%);
    color: var(--ink-light);
  }
  .contact {
    position: absolute; right: 48px; top: 36px; text-align: right;
    font-family: "Montserrat", sans-serif;
  }
  .contact__name { font-size: 28px; font-weight: 700; letter-spacing: .5px; margin-bottom: 30px; }
  .contact__line { font-size: 17px; font-weight: 400; line-height: 1.35; letter-spacing: .3px; }
  .title-block {
    position: absolute; left: 58px; top: 200px; text-align: center;
  }
  .title-block__service {
    font-family: "Open Sans", sans-serif; font-style: italic; font-weight: 700;
    font-size: 32px; letter-spacing: .3px;
  }
  .title-block__license {
    font-family: "Montserrat", sans-serif; font-size: 19px; font-weight: 400;
    letter-spacing: .8px; margin-top: -4px;
  }
  /* Card back */
  .card--back { background: var(--night-bottom); }
  .scene {
    position: absolute; inset: 0;
    background:
      radial-gradient(ellipse 40% 30% at 70% 40%, rgba(90,130,230,.45), transparent 70%),
      linear-gradient(180deg, var(--night-top) 0%, var(--night-mid) 40%, #1a2c6a 70%, var(--night-bottom) 100%);
  }
  .signature {
    position: absolute; left: 0; right: 0; bottom: 38px;
    display: flex; align-items: center; gap: 14px;
  }
  .signature__rule { height: 2px; background: var(--ink-light); }
  .signature__rule--long { flex: 1; }
  .signature__rule--short { width: 28px; }
  .signature__text {
    font-family: "Great Vibes", cursive; color: var(--ink-light);
    font-size: 40px; line-height: 1; transform: translateY(-8px);
  }
</style>
</head>
<body>
<main class="canvas">
  <section class="card card--front">
    <div class="contact">
      <p class="contact__name">MARA VELLIS</p>
      <p class="contact__line">000 314 958</p>
      <p class="contact__line">www.skyviewframeworks</p>
    </div>
    <div class="title-block">
      <p class="title-block__service">Aerial Photography</p>
      <p class="title-block__license">ZQB# 90817263</p>
    </div>
  </section>

  <section class="card card--back">
    <div class="scene" role="img" aria-label="Photo of a white quadcopter drone flying over a blurred night city skyline"></div>
    <div class="signature">
      <span class="signature__rule signature__rule--long"></span>
      <span class="signature__text">Aerial Photography</span>
      <span class="signature__rule signature__rule--short"></span>
    </div>
  </section>
</main>
</body>
</html>
```